Business card for a vending machine business

I need a business card for my vending machine business. The name is Kestrel Snackworks, LLC. The card is one-sided, and landscape format. Not portrait.

The information for the card is as follows:

Dana Whitlow
Owner
(555) 314-2907
Kestrelsnackworks.example
Info@kestrelsnackworks.example

I'd like colors and design elements to match what's in my logo and company name. I'd like to have the checkered flag or racing stripe if possible You can use a border if youd like. You can use a background color if it looks nice and doesn't clash with the logo
Use your creativity. But a white background is perfectly fine. The card can be as simple, yet gets the point across to match the company name and logo.

I uploaded a copy of my logo. I also uploaded a businesses card I started to create, but since it was missing something, I gave up. Another upload has a red thunderbolt and the checkerer flag. Those two uploads are for inspiration. Again, please make sure to make the card landscape, not portrait. Thank you, designers. Good luck to all.

```html
<!DOCTYPE html>
<html lang="en">
<head>
<meta charset="utf-8">
<title>Kestrel Snackworks – Business Card</title>
<link rel="stylesheet" href="https://fonts.googleapis.com/css2?family=Lato:wght@400;700&display=swap">
<style>
  :root {
    --card-bg: #fbfbfb;
    --brand-red: #e8262b;
    --ink: #3f3f44;
    --ink-dark: #1e1e22;
    --flag-dark: #2b2b30;
  }
  * { margin: 0; padding: 0; box-sizing: border-box; }
  html, body {
    width: 1200px; height: 734px; overflow: hidden;
    background: var(--card-bg);
    font-family: "Lato", sans-serif;
  }
  .card {
    position: relative;
    width: 1200px; height: 734px;
    background: var(--card-bg);
  }
  .brand {
    position: absolute;
    left: 0; right: 0; top: 215px;
    display: flex; align-items: center; justify-content: center; gap: 18px;
  }
  .brand-mark {
    width: 34px; height: 34px;
    background: var(--brand-red);
  }
  .brand-name {
    font-weight: 700;
    font-size: 62px;
    color: var(--brand-red);
    letter-spacing: 0.5px;
    line-height: 1;
  }
  .identity {
    position: absolute;
    right: 653px; top: 508px;
    text-align: right;
  }
  .person-name {
    font-weight: 700;
    font-size: 52px;
    color: var(--brand-red);
    line-height: 1;
    text-transform: uppercase;
  }
  .person-role {
    font-weight: 400;
    font-size: 30px;
    color: var(--ink);
    margin-top: 10px;
    letter-spacing: 1px;
  }
  .divider {
    position: absolute;
    left: 589px; top: 496px;
    width: 3px; height: 114px;
    background: var(--brand-red);
  }
  .contacts {
    position: absolute;
    left: 640px; top: 488px;
    list-style: none;
  }
  .contact-item {
    display: flex; align-items: center; gap: 15px;
    height: 44px;
    font-size: 27px;
    color: var(--ink);
    letter-spacing: 0.8px;
  }
  .contact-icon { width: 22px; height: 22px; flex: none; }
  .finish-band {
    position: absolute;
    left: 0; bottom: 0;
    width: 100%; height: 44px;
    display: flex;
  }
  .finish-band .band-dark {
    width: 587px;
    background: linear-gradient(90deg, #6e6e74, var(--flag-dark) 50%, #6e6e74);
  }
  .finish-band .band-red {
    flex: 1;
    background: linear-gradient(90deg, #f07a7c, var(--brand-red) 50%, #f07a7c);
  }
</style>
</head>
<body>
  <main class="card">
    <div class="brand">
      <span class="brand-mark"></span>
      <span class="brand-name">Kestrel Snackworks</span>
    </div>

    <div class="identity">
      <p class="person-name">Dana Whitlow</p>
      <p class="person-role">Owner</p>
    </div>

    <div class="divider"></div>

    <ul class="contacts">
      <li class="contact-item">
        <svg class="contact-icon" viewBox="0 0 24 24" aria-hidden="true">
          <path fill="#e8262b" d="M6.6 10.8a15.1 15.1 0 0 0 6.6 6.6l2.2-2.2c.3-.3.7-.4 1-.2 1.1.4 2.3.6 3.6.6.6 0 1 .4 1 1V20c0 .6-.4 1-1 1A17 17 0 0 1 3 4c0-.6.4-1 1-1h3.5c.6 0 1 .4 1 1 0 1.3.2 2.5.6 3.6.1.3 0 .7-.2 1z"/>
        </svg>
        <span>(555) 314-2907</span>
      </li>
      <li class="contact-item">
        <svg class="contact-icon" viewBox="0 0 24 24" aria-hidden="true">
          <rect x="2" y="5" width="20" height="14" rx="1.5" fill="#e8262b"/>
          <path d="M3 6.5l9 6.5 9-6.5" fill="none" stroke="#fff" stroke-width="1.6"/>
        </svg>
        <span>Info@kestrelsnackworks.example</span>
      </li>
      <li class="contact-item">
        <svg class="contact-icon" viewBox="0 0 24 24" aria-hidden="true">
          <circle cx="12" cy="12" r="10" fill="#e8262b"/>
          <path d="M2 12h20M12 2c3 3 3 17 0 20M12 2c-3 3-3 17 0 20" fill="none" stroke="#fff" stroke-width="1.4"/>
        </svg>
        <span>Kestrelsnackworks.example</span>
      </li>
    </ul>

    <div class="finish-band" role="img" aria-label="Checkered racing flag stripe, black and white on the left, red and white on the right">
      <div class="band-dark"></div>
      <div class="band-red"></div>
    </div>
  </main>
</body>
</html>
```